Rural photograpy business card design

I need a business card for my photography business, marisol dovey photography. I would like my logo and pre designed font used on the card. Also my business specialises in photographing rural australia (e.g. shearing sheds, livestock, landscapes, farms), so a rural or country feel to the card would be great. I would like to keep the colours fresh but not too overpowering or juvenile.

Hi,

Could you please add my facebook page to the card - www.snapfolk.net/Marisol/Dovey/Photography.
Thanks,
Marisol.

Reason: I have uploaded two photos I would like either one used on the card.

Target Market(s)

Farmers, country people from their mid twenties onwards

Industry/Entity Type

Business

Contact Information for Business Card

Marisol Dovey Photography. Marisol Pendergast. 1295 Wirrabilla-Kontee Road, Kontee Qld 4871. 0471620394.

Requirements
Must have
• My pre-designed logo and font. Also please add my facebook address - www.snapfolk.net/MarisolDovey/Photography.
Please use one of the photos I have provided.
Should not have
• Peoples faces on the card.

```html
<!DOCTYPE html>
<html lang="en">
<head>
<meta charset="utf-8">
<title>Marisol Dovey Photography – Business Cards</title>
<link href="https://fonts.googleapis.com/css2?family=Josefin+Sans:wght@300;400&display=swap" rel="stylesheet">
<style>
  :root {
    --backdrop: #2c2c2c;
    --sky-top: #2f5fb8;
    --sky-mid: #8fb0d8;
    --field-gold: #c9a055;
    --field-green: #5f9a2c;
    --field-dark: #35601c;
    --band-light: rgba(245, 245, 245, 0.82);
    --band-green: rgba(128, 186, 60, 0.85);
    --panel-green: rgba(150, 205, 70, 0.72);
    --strip-light: rgba(235, 238, 240, 0.72);
    --ink: #2a2a2a;
    --ink-soft: #3d3d3d;
    --paper: #ffffff;
  }
  * { margin: 0; padding: 0; box-sizing: border-box; }
  html, body { width: 1000px; height: 1200px; overflow: hidden; }
  body {
    background: var(--backdrop);
    font-family: "Josefin Sans", sans-serif;
    position: relative;
  }
  .card {
    position: absolute;
    left: 194px;
    width: 612px;
    height: 350px;
    overflow: hidden;
  }
  .card--front-colour { top: 39px; }
  .card--front-mono { top: 424px; }
  .card--back { top: 807px; }

  .photo { position: absolute; inset: 0; }
  .photo--farm-colour {
    background: linear-gradient(180deg, var(--sky-top) 0%, var(--sky-mid) 40%, #d8e2ea 48%, #3f6d25 52%, var(--field-gold) 62%, var(--field-green) 72%, var(--field-dark) 100%);
  }
  .photo--farm-mono {
    background: linear-gradient(180deg, #3a3a3a 0%, #9a9a9a 40%, #d0d0d0 48%, #3a3a3a 52%, #8a8a8a 62%, #7a7a7a 75%, #4a4a4a 100%);
  }
  .photo--sunset-field {
    background: linear-gradient(180deg, #3d6fae 0%, #8fb3d9 45%, #d9c9a8 55%, #b48a4a 70%, #6b5a2c 100%);
  }

  .logo-band {
    position: absolute;
    left: 0; right: 0;
    top: 86px; height: 85px;
    background: var(--band-light);
  }
  .logo-dot {
    position: absolute;
    left: 140px; top: 13px;
    width: 60px; height: 60px;
    border-radius: 50%;
    background: var(--ink);
  }
  .logo-name {
    position: absolute;
    left: 236px; top: 10px;
    width: 270px;
    font-weight: 300;
    font-size: 26px;
    line-height: 33px;
    letter-spacing: 1.8px;
    color: var(--ink);
    text-transform: uppercase;
    white-space: nowrap;
  }
  .logo-name span { display: block; }
  .name-band {
    position: absolute;
    left: 0; right: 0;
    top: 174px; height: 27px;
    background: var(--band-green);
    display: flex; align-items: center; justify-content: center;
  }
  .name-band span {
    font-weight: 300;
    font-size: 20px;
    letter-spacing: 2.5px;
    color: var(--paper);
    text-transform: uppercase;
    padding-top: 3px;
  }

  .icon-strip {
    position: absolute;
    left: 99px; top: 0;
    width: 85px; height: 350px;
    background: var(--strip-light);
  }
  .info-panel {
    position: absolute;
    left: 184px; top: 0;
    width: 327px; height: 350px;
    background: var(--panel-green);
  }
  .info-row {
    position: absolute;
    left: 99px;
    width: 412px;
  }
  .info-row .rule {
    position: absolute;
    left: 0; right: 0;
    height: 22px;
    background: rgba(255,255,255,0.14);
  }
  .info-row svg { position: absolute; left: 25px; }
  .info-title {
    position: absolute;
    left: 106px;
    font-weight: 300;
    font-size: 23px;
    color: var(--ink-soft);
    white-space: nowrap;
  }
  .info-detail {
    position: absolute;
    left: 106px;
    font-weight: 300;
    font-size: 15px;
    line-height: 19px;
    letter-spacing: 0.6px;
    color: var(--paper);
    padding-left: 15px;
    white-space: nowrap;
  }
  .info-detail::before {
    content: "";
    position: absolute;
    left: 0; top: 4px;
    border-left: 6px solid var(--ink-soft);
    border-top: 4px solid transparent;
    border-bottom: 4px solid transparent;
  }
</style>
</head>
<body>

<section class="card card--front-colour">
  <div class="photo photo--farm-colour" role="img" aria-label="Photograph of green farm paddock with a dark timber fence under a blue sky"></div>
  <div class="logo-band">
    <span class="logo-dot"></span>
    <div class="logo-name"><span>Marisol Dovey</span><span>Photography</span></div>
  </div>
  <div class="name-band"><span>Marisol Pendergast</span></div>
</section>

<section class="card card--front-mono">
  <div class="photo photo--farm-mono" role="img" aria-label="Black and white photograph of farm paddock with timber fence and cloudy sky"></div>
  <div class="logo-band">
    <span class="logo-dot"></span>
    <div class="logo-name"><span>Marisol Dovey</span><span>Photography</span></div>
  </div>
  <div class="name-band"><span>Marisol Pendergast</span></div>
</section>

<section class="card card--back">
  <div class="photo photo--sunset-field" role="img" aria-label="Photograph of a rural field with a tree at sunset"></div>
  <div class="icon-strip"></div>
  <div class="info-panel"></div>

  <div class="info-row" style="top:60px">
    <div class="rule" style="top:22px"></div>
    <svg width="32" height="34" viewBox="0 0 32 34" aria-hidden="true">
      <circle cx="16" cy="10" r="8" fill="rgba(255,255,255,0.85)"/>
      <path d="M2 34 C2 22 30 22 30 34 Z" fill="rgba(255,255,255,0.85)"/>
    </svg>
    <div class="info-title" style="top:2px">Marisol Pendergast</div>
    <div class="info-detail" style="top:33px">photographer</div>
  </div>

  <div class="info-row" style="top:152px">
    <div class="rule" style="top:22px"></div>
    <svg width="36" height="26" viewBox="0 0 36 26" aria-hidden="true" style="top:4px">
      <rect x="1" y="1" width="34" height="24" fill="none" stroke="rgba(255,255,255,0.85)" stroke-width="2"/>
      <path d="M1 1 L18 15 L35 1" fill="none" stroke="rgba(255,255,255,0.85)" stroke-width="2"/>
    </svg>
    <div class="info-title" style="top:2px">Contact Me</div>
    <div class="info-detail" style="top:33px">0471620394</div>
  </div>

  <div class="info-row" style="top:246px">
    <div class="rule" style="top:22px"></div>
    <svg width="26" height="36" viewBox="0 0 26 36" aria-hidden="true" style="left:28px">
      <path d="M13 35 C13 35 1 20 1 12 A12 12 0 0 1 25 12 C25 20 13 35 13 35 Z" fill="rgba(255,255,255,0.8)"/>
      <circle cx="13" cy="12" r="4.5" fill="rgba(150,205,70,0.9)"/>
    </svg>
    <div class="info-title" style="top:2px">Address</div>
    <div class="info-detail" style="top:33px">1295 Wirrabilla-Kontee Road,<br>Kontee Qld 4871</div>
  </div>
</section>

</body>
</html>
```